i need a Star Bulletin blog design

hi, i need a blog which have Star Bulletin news. My blog should be attractive and mature with a good theme. Readers of my blog should be able to comment. You can include any attractive colour (blue, green, purple, red).

Target Market(s)

Celebrity fans and enthusiasts

Industry/Entity Type

News

```html
<!DOCTYPE html>
<html lang="en">
<head>
<meta charset="utf-8">
<title>Star Bulletin</title>
<link href="https://fonts.googleapis.com/css2?family=Roboto:ital,wght@0,400;0,500;0,700;1,400&display=swap" rel="stylesheet">
<style>
:root{
  --blue:#0c4a92;
  --blue-dark:#0a3f7d;
  --green:#43a535;
  --hero-bg:#e3e3e3;
  --card-bg:#f3f3f3;
  --text:#222;
  --muted:#7a7a7a;
  --line:#e2e2e2;
  --social-a:#3e5c9b;
  --social-b:#2f9ce6;
  --social-c:#e0283a;
}
*{box-sizing:border-box;margin:0;padding:0}
html,body{width:1200px;height:3203px;overflow:hidden}
body{position:relative;background:#fff;font-family:'Roboto',sans-serif;color:var(--text)}
.abs{position:absolute}

/* header */
.site-header{left:0;top:0;width:1200px;height:103px}
.brand{left:100px;top:36px;font-size:30px;font-weight:500;letter-spacing:.5px;color:#111;text-transform:uppercase}
.follow{right:102px;top:42px;display:flex;align-items:center;gap:12px;font-size:13px;color:#333}
.follow .dot{width:16px;height:16px;border-radius:50%;background:#b4b4b4}
.accent-line{left:0;top:103px;width:1200px;height:5px;background:var(--green)}
.main-nav{left:0;top:108px;width:1200px;height:53px;background:var(--blue)}
.main-nav ul{list-style:none;display:flex;position:absolute;left:100px;top:0;height:53px;align-items:center}
.main-nav li{color:#fff;font-size:13px;font-weight:500;text-transform:uppercase}
.search-btn{position:absolute;left:1048px;top:0;width:49px;height:53px;background:var(--blue-dark);display:flex;align-items:center;justify-content:center}

/* hero */
.hero{left:0;top:161px;width:1200px;height:480px;background:var(--hero-bg)}
.tile{position:absolute;overflow:hidden}
.tile .shade{position:absolute;inset:0}
.tag{display:inline-block;background:var(--blue);color:#fff;font-size:11px;font-weight:500;text-transform:uppercase;padding:9px 12px}
.tile .cap{position:absolute;left:16px;bottom:16px;right:6px;color:#fff}
.tile .cap h3{font-size:11.5px;font-weight:500;text-transform:uppercase;margin-top:14px;white-space:nowrap}
.tile.big .cap{left:34px;bottom:26px;right:20px}
.tile.big .cap h3{font-size:15px;margin-top:22px}
.tile .cap p{font-size:13px;margin-top:6px}
.dots{position:absolute;left:563px;top:445px;display:flex;gap:3px}
.dots span{width:14px;height:14px;border-radius:50%;background:#fff}
.dots span.on{background:#555}

/* section heads */
.band-head{background:var(--blue);color:#fff;font-size:14px;font-weight:700;text-transform:uppercase;display:flex;align-items:center;justify-content:center;height:58px;width:660px;left:100px}
.side-head{font-size:16px;font-weight:700;color:var(--blue);text-transform:uppercase}
.side-head::after{content:"";display:block;width:50px;height:4px;background:var(--blue);margin-top:12px}

/* post rows */
.post-row{left:100px;width:660px;height:214px;display:flex;background:var(--card-bg)}
.post-row .photo{width:278px;height:214px;flex:none}
.post-row .body{padding:18px 28px 0 30px}
.post-row h2{font-size:15px;font-weight:700;text-transform:uppercase;line-height:1.45}
.meta{font-size:12px;color:var(--muted);margin-top:8px}
.meta i{font-style:normal;margin:0 8px;color:#bbb}
.post-row p{font-size:13.5px;line-height:1.7;margin-top:16px;color:#333}
.more{font-size:12px;font-weight:700;text-transform:uppercase;margin-top:14px;display:flex;align-items:center;gap:8px;letter-spacing:.5px}
.more::after{content:"";border-left:5px solid #222;border-top:4px solid transparent;border-bottom:4px solid transparent}

.rule{left:100px;top:1517px;width:660px;height:1px;background:#ccc}

/* category cards */
.cat-card{top:1573px;width:316px;height:690px;background:var(--card-bg)}
.cat-card .lead{position:relative;height:240px}
.cat-card .lead .cap{position:absolute;left:20px;bottom:28px;color:#fff}
.cat-card .lead .cap h3{font-size:13px;font-weight:500;text-transform:uppercase;margin-top:12px}
.cat-card .lead .cap p{font-size:11px;font-style:italic;margin-top:4px}
.mini{display:flex;gap:16px;padding:0 16px;height:98px;align-items:flex-start}
.lead + .mini{margin-top:18px}
.mini .thumb{width:96px;height:70px;flex:none}
.mini h4{font-size:13px;font-weight:400;line-height:1.45;margin-top:4px}
.mini span{display:block;font-size:11px;font-style:italic;color:var(--muted);margin-top:6px}
.pager{position:absolute;left:16px;bottom:16px;display:flex;gap:4px}
.pager span{width:30px;height:30px;background:#ddd;display:flex;align-items:center;justify-content:center}

/* sidebar */
.side{left:788px;width:309px}
.pop-item{display:flex;gap:16px;height:105px;border-bottom:1px solid var(--line)}
.pop-item .thumb{width:56px;height:50px;flex:none}
.pop-item h4{font-size:13px;font-weight:400;line-height:1.45;color:#222}
.pop-item span{display:block;font-size:11px;color:var(--muted);margin-top:8px}
.archive li{list-style:none;font-size:13px;height:46px;line-height:46px;border-bottom:1px solid var(--line);padding-left:4px}
.tabs{border:1px solid #ddd;height:685px;overflow:hidden}
.tabs .tab-bar{display:flex;height:40px;background:#f1f1f1;border-bottom:1px solid #ddd}
.tabs .tab-bar span{flex:1;display:flex;align-items:center;justify-content:center;font-size:13px;border-left:1px solid #ddd}
.tabs .tab-bar span:first-child{background:#fff;border-left:none}
.tab-item{height:107px;border-bottom:1px solid var(--line);padding:18px 30px 0 42px;position:relative}
.tab-item:last-child{border-bottom:none}
.tab-item::before{content:"";position:absolute;left:22px;top:23px;border-left:5px solid #333;border-top:4px solid transparent;border-bottom:4px solid transparent}
.tab-item h4{font-size:13px;font-weight:400;line-height:1.45}
.tab-item span{display:block;font-size:11px;color:var(--muted);margin-top:6px}
.social-btn{left:788px;width:309px;height:64px;display:flex;align-items:center;color:#fff;font-size:14px;font-weight:500;text-transform:uppercase;white-space:nowrap}
.social-btn .sq{width:16px;height:16px;background:#fff;margin:0 39px 0 28px;flex:none}

/* footer */
.site-footer{left:0;top:3128px;width:1200px;height:75px;background:var(--blue);color:#fff;font-size:13px;display:flex;align-items:center;justify-content:center}
</style>
</head>
<body>

<header class="site-header abs">
  <div class="brand abs">Star Bulletin</div>
  <div class="follow abs">Follow Us On <span class="dot"></span><span class="dot"></span><span class="dot"></span></div>
</header>
<div class="accent-line abs"></div>
<nav class="main-nav abs">
  <ul>
    <li style="width:90px">Home</li>
    <li style="width:97px">About</li>
    <li style="width:119px">Articles</li>
    <li style="width:140px">Interviews</li>
    <li style="width:77px">News</li>
    <li style="width:114px">Gossips</li>
    <li style="width:106px">Events</li>
    <li>Contact</li>
  </ul>
  <div class="search-btn"><svg width="16" height="16" viewBox="0 0 16 16"><circle cx="6.5" cy="6.5" r="4.5" fill="none" stroke="#fff" stroke-width="2"/><line x1="10" y1="10" x2="14" y2="14" stroke="#fff" stroke-width="2.2" stroke-linecap="round"/></svg></div>
</nav>

<section class="hero abs">
  <div class="tile big" style="left:100px;top:35px;width:549px;height:395px">
    <div class="shade" role="img" aria-label="Man in glasses listening through a paper tube" style="background:linear-gradient(135deg,#7e7a76,#4a4946 55%,#2e2d2b)"></div>
    <div class="cap"><span class="tag">Gossips</span><h3>Lorem ipsum is simply dummy text of the printing</h3><p>Contrary to popular belief, Lorem Ipsum</p></div>
  </div>
  <div class="tile" style="left:649px;top:35px;width:223px;height:197px">
    <div class="shade" role="img" aria-label="Businessman in a suit" style="background:linear-gradient(135deg,#6c7378,#3d4246)"></div>
    <div class="cap"><span class="tag">Interviews</span><h3>Lorem ipsum is simply dummy</h3></div>
  </div>
  <div class="tile" style="left:872px;top:35px;width:223px;height:197px">
    <div class="shade" role="img" aria-label="Camera recording a broadcast" style="background:linear-gradient(135deg,#2f6e86,#143444)"></div>
    <div class="cap"><span class="tag">News</span><h3>Lorem ipsum is simply dummy</h3></div>
  </div>
  <div class="tile" style="left:649px;top:232px;width:223px;height:198px">
    <div class="shade" role="img" aria-label="Hand writing with a pen" style="background:linear-gradient(135deg,#9a9ea3,#5d6166)"></div>
    <div class="cap"><span class="tag">Articles</span><h3>Lorem ipsum is simply dummy</h3></div>
  </div>
  <div class="tile" style="left:872px;top:232px;width:223px;height:198px">
    <div class="shade" role="img" aria-label="Folded newspaper" style="background:linear-gradient(135deg,#8fa8c2,#4b6684)"></div>
    <div class="cap"><span class="tag">Articles</span><h3>Lorem ipsum is simply dummy</h3></div>
  </div>
  <div class="dots"><span></span><span class="on"></span><span></span><span></span></div>
</section>

<!-- latest articles -->
<div class="band-head abs" style="top:670px">Latest Articles</div>

<article class="post-row abs" style="top:756px">
  <div class="photo" role="img" aria-label="Couple looking through binoculars" style="background:linear-gradient(135deg,#8c8a80,#5c6a68)"></div>
  <div class="body">
    <h2>There are many variations of passages of Lorem</h2>
    <div class="meta">24 Jan 2015 by John Doe<i>|</i>2 Comments</div>
    <p>The standard chunk of Lorem Ipsum used since the 1500s is reproduced below for those interested. Sections 1.10.32 and 1.10.33 from "de Finibus</p>
    <div class="more">Read more</div>
  </div>
</article>
<article class="post-row abs" style="top:999px">
  <div class="photo" role="img" aria-label="Man reading a newspaper" style="background:linear-gradient(135deg,#7d8a96,#3e4953)"></div>
  <div class="body">
    <h2>There are many variations of passages of Lorem</h2>
    <div class="meta">24 Jan 2015 by John Doe<i>|</i>2 Comments</div>
    <p>The standard chunk of Lorem Ipsum used since the 1500s is reproduced below for those interested. Sections 1.10.32 and 1.10.33 from "de Finibus</p>
    <div class="more">Read more</div>
  </div>
</article>
<article class="post-row abs" style="top:1247px">
  <div class="photo" role="img" aria-label="Laptop showing breaking news" style="background:linear-gradient(135deg,#a84a42,#5a4642)"></div>
  <div class="body">
    <h2>There are many variations of passages of Lorem</h2>
    <div class="meta">24 Jan 2015 by John Doe<i>|</i>2 Comments</div>
    <p>The standard chunk of Lorem Ipsum used since the 1500s is reproduced below for those interested. Sections 1.10.32 and 1.10.33 from "de Finibus</p>
    <div class="more">Read more</div>
  </div>
</article>

<div class="rule abs"></div>

<!-- category cards -->
<section class="cat-card abs" style="left:100px">
  <div class="lead">
    <div role="img" aria-label="Two women whispering gossip" style="position:absolute;inset:0;background:linear-gradient(135deg,#6e5a52,#3a3434)"></div>
    <div class="cap"><span class="tag">Gossips</span><h3>Lorem ipsum is simply dummy</h3><p>24 Jan 2015/John Doe/5 Comments</p></div>
  </div>
  <div class="mini"><div class="thumb" role="img" aria-label="Woman listening" style="background:linear-gradient(135deg,#7a6a60,#443a36)"></div><div><h4>There are many variations of passages of Lorem Ipsum</h4><span>24 Jan 2015 by John Doe</span></div></div>
  <div class="mini"><div class="thumb" role="img" aria-label="Woman with megaphone" style="background:linear-gradient(135deg,#b7c27a,#6a8a66)"></div><div><h4>There are many variations of passages of Lorem Ipsum</h4><span>24 Jan 2015 by John Doe</span></div></div>
  <div class="mini"><div class="thumb" role="img" aria-label="Friends chatting" style="background:linear-gradient(135deg,#9ab36a,#5a7446)"></div><div><h4>There are many variations of passages of Lorem Ipsum</h4><span>24 Jan 2015 by John Doe</span></div></div>
  <div class="mini"><div class="thumb" role="img" aria-label="Group of people talking" style="background:linear-gradient(135deg,#8a7a6a,#4e4a44)"></div><div><h4>There are many variations of passages of Lorem Ipsum</h4><span>24 Jan 2015 by John Doe</span></div></div>
  <div class="pager"><span><svg width="8" height="10"><path d="M6 1L2 5l4 4" fill="none" stroke="#777" stroke-width="1.5"/></svg></span><span><svg width="8" height="10"><path d="M2 1l4 4-4 4" fill="none" stroke="#777" stroke-width="1.5"/></svg></span></div>
</section>
<section class="cat-card abs" style="left:446px">
  <div class="lead">
    <div role="img" aria-label="People waiting for interviews" style="position:absolute;inset:0;background:linear-gradient(135deg,#5f6a7c,#2e3440)"></div>
    <div class="cap"><span class="tag">Interviews</span><h3>Lorem ipsum is simply dummy</h3><p>24 Jan 2015/John Doe/5 Comments</p></div>
  </div>
  <div class="mini"><div class="thumb" role="img" aria-label="Woman surprised" style="background:linear-gradient(135deg,#7a6a60,#443a36)"></div><div><h4>There are many variations of passages of Lorem Ipsum</h4><span>24 Jan 2015 by John Doe</span></div></div>
  <div class="mini"><div class="thumb" role="img" aria-label="Woman on the phone" style="background:linear-gradient(135deg,#8a7468,#3e3230)"></div><div><h4>There are many variations of passages of Lorem Ipsum</h4><span>24 Jan 2015 by John Doe</span></div></div>
  <div class="mini"><div class="thumb" role="img" aria-label="Three colleagues" style="background:linear-gradient(135deg,#9a8678,#5a4a42)"></div><div><h4>There are many variations of passages of Lorem Ipsum</h4><span>24 Jan 2015 by John Doe</span></div></div>
  <div class="mini"><div class="thumb" role="img" aria-label="Smiling woman" style="background:linear-gradient(135deg,#b5a69a,#6e5e54)"></div><div><h4>There are many variations of passages of Lorem Ipsum</h4><span>24 Jan 2015 by John Doe</span></div></div>
  <div class="pager"><span><svg width="8" height="10"><path d="M6 1L2 5l4 4" fill="none" stroke="#777" stroke-width="1.5"/></svg></span><span><svg width="8" height="10"><path d="M2 1l4 4-4 4" fill="none" stroke="#777" stroke-width="1.5"/></svg></span></div>
</section>

<!-- latest news -->
<div class="band-head abs" style="top:2299px">Latest News</div>

<article class="post-row abs" style="top:2385px">
  <div class="photo" role="img" aria-label="Business people applauding" style="background:linear-gradient(135deg,#8a7c70,#4a4a4e)"></div>
  <div class="body">
    <h2>There are many variations of passages of Lorem</h2>
    <div class="meta">24 Jan 2015 by John Doe<i>|</i>2 Comments</div>
    <p>The standard chunk of Lorem Ipsum used since the 1500s is reproduced below for those interested. Sections 1.10.32 and 1.10.33 from "de Finibus</p>
    <div class="more">Read more</div>
  </div>
</article>
<article class="post-row abs" style="top:2628px">
  <div class="photo" role="img" aria-label="Hand touching a network of contacts" style="background:linear-gradient(135deg,#2c4a70,#0e1a2c)"></div>
  <div class="body">
    <h2>There are many variations of passages of Lorem</h2>
    <div class="meta">24 Jan 2015 by John Doe<i>|</i>2 Comments</div>
    <p>The standard chunk of Lorem Ipsum used since the 1500s is reproduced below for those interested. Sections 1.10.32 and 1.10.33 from "de Finibus</p>
    <div class="more">Read more</div>
  </div>
</article>
<article class="post-row abs" style="top:2876px">
  <div class="photo" role="img" aria-label="Laptop showing a news site" style="background:linear-gradient(135deg,#5a7aa8,#23385a)"></div>
  <div class="body">
    <h2>There are many variations of passages of Lorem</h2>
    <div class="meta">24 Jan 2015 by John Doe<i>|</i>2 Comments</div>
    <p>The standard chunk of Lorem Ipsum used since the 1500s is reproduced below for those interested. Sections 1.10.32 and 1.10.33 from "de Finibus</p>
    <div class="more">Read more</div>
  </div>
</article>

<!-- sidebar -->
<div class="side side-head abs" style="top:684px">Popular Post</div>
<div class="side abs" style="top:752px">
  <div class="pop-item"><div class="thumb" role="img" aria-label="Woman portrait" style="background:linear-gradient(135deg,#8a7a70,#3a3430)"></div><div><h4>There are many variations of passages of Lorem Ipsum available</h4><span>JAN 28,2015</span></div></div>
  <div class="pop-item"><div class="thumb" role="img" aria-label="Newspaper stack" style="background:linear-gradient(135deg,#c8c4bc,#7a766e)"></div><div><h4>Contrary to popular belief, Lorem Ipsum is not simply</h4><span>JAN 28,2015</span></div></div>
  <div class="pop-item"><div class="thumb" role="img" aria-label="Woman portrait" style="background:linear-gradient(135deg,#9a8a80,#4a3e38)"></div><div><h4>There are many variations of passages of Lorem Ipsum</h4><span>JAN 28,2015</span></div></div>
  <div class="pop-item"><div class="thumb" role="img" aria-label="Woman portrait" style="background:linear-gradient(135deg,#8a7468,#342a26)"></div><div><h4>Sed ut perspiciatis unde omnis iste natus error sit voluptatem accusantium</h4><span>JAN 28,2015</span></div></div>
  <div class="pop-item"><div class="thumb" role="img" aria-label="Person reading" style="background:linear-gradient(135deg,#a09a94,#5a5450)"></div><div><h4>But I must explain to you how all this mistaken idea of denouncing</h4><span>JAN 28,2015</span></div></div>
  <div class="pop-item" style="border-bottom:none"><div class="thumb" role="img" aria-label="Tablet with news" style="background:linear-gradient(135deg,#3a5a8a,#1a2a40)"></div><div><h4>At vero eos et accusamus et iusto odio dignissimos ducimus qui blanditiis</h4><span>JAN 28,2015</span></div></div>
</div>

<div class="side side-head abs" style="top:1390px">Archives</div>
<ul class="side archive abs" style="top:1437px">
  <li>May 2014</li><li>April 2014</li><li>March 2014</li><li>February 2014</li><li style="border-bottom:none">January 2014</li>
</ul>

<div class="side tabs abs" style="top:1700px">
  <div class="tab-bar"><span>Popular</span><span>Recent</span><span>Comments</span></div>
  <div class="tab-item"><h4>At vero eos et accusamus et iusto odio dignissimos ducimus qui blanditiis</h4><span>JAN 28,2015</span></div>
  <div class="tab-item"><h4>At vero eos et accusamus et iusto odio dignissimos ducimus qui blanditiis</h4><span>JAN 28,2015</span></div>
  <div class="tab-item"><h4>On the other hand, we denounce with righteous indignation and dislike men who</h4><span>JAN 28,2015</span></div>
  <div class="tab-item"><h4>At vero eos et accusamus et iusto odio dignissimos ducimus qui blanditiis praesentium</h4><span>JAN 28,2015</span></div>
  <div class="tab-item"><h4>On the other hand, we denounce with righteous indignation and dislike men who</h4><span>JAN 28,2015</span></div>
  <div class="tab-item"><h4>On the other hand, we denounce with righteous indignation and dislike men who</h4><span>JAN 28,2015</span></div>
</div>

<div class="social-btn abs" style="top:2412px;background:var(--social-a)"><span class="sq"></span>Like us on Friendbook</div>
<div class="social-btn abs" style="top:2489px;background:var(--social-b)"><span class="sq"></span>Follow us on Chirper</div>
<div class="social-btn abs" style="top:2566px;background:var(--social-c)"><span class="sq"></span>Follow us on Circles Plus</div>

<footer class="site-footer abs">Copyrights @ 2015 All Rights Reserved</footer>

</body>
</html>
```